Corporate Material
Powerpoint/Word-Manual Templates
#21 can you remove the globe image and use a more modern theme and incorporate more cloud and technology type images.
#17 can you make the logo in the bottom left corners a little smaller I do not want the logo to over power the presentation. Also i would like to see the manual.
Also can you add a few cloud images to your presentation cover.
#16 please show me a example of a page with the subject header and body
Contest is extended for 2 more days.
-Ruth
I am interested in have a custom powerpoint template design for my company.
We are a technology company looking for a template that will allow us to introduce ourselves to prospective customers.
Innovation, Cloud Computing and Cloud Lifecycle Management.
Out target customer is the Public Sector (Government Customers)
The microsoft word template is a word template that will be used to developed corporate manuals so looking for a clean corporate cover page design and formatted header a footer.
1. Powerpoint Presentation
The presentation Title Master should have images of innovative technology to include cloud, government, and management consulting images.
I would like to see on the slide pages a header area that has technology images in the right corner so a title can be added to the slide.
The footer of the slide should have a subdued corporate logo in the bottom left corner.
I hope this helps.
This will be used as a corporate capabilities statement presentation
I would need more detailed scheme of the structure of Word Teplate. I've made one draft, but it could be way better if I know what exactly is my job.
Kindly give the link of your website,,
Dlpn-us site info
Designers I have not had any input on this effort.....
Innovative, technology focused images but a clean corporate look.
Ok, designers I am looking for presentations that will provide customers with a mature innovative technology company. So I am looking for some clean corporate images to be part of the templates. please review company website for additional details if required.
Looking for Executive Briefing powerpoint template and microsoft word template is what i am looking for.

```html
<!DOCTYPE html>
<html lang="en">
<head>
<meta charset="utf-8">
<title>DLPN Corporate Templates</title>
<link href="https://fonts.googleapis.com/css2?family=Open+Sans:ital,wght@0,400;0,600;0,700;1,400&display=swap" rel="stylesheet">
<style>
:root{
  --stage:#e6e7e9;
  --page:#ffffff;
  --brand:#1d5fae;
  --brand-dark:#0c3a7a;
  --brand-light:#5ea3df;
  --sky:#cfe3f5;
  --ink:#3a3a3a;
  --muted:#7d8590;
  --rule:#9fc2e6;
}
*{box-sizing:border-box;margin:0;padding:0}
html,body{width:1200px;height:965px;overflow:hidden;background:var(--stage);font-family:"Open Sans",Arial,sans-serif;color:var(--ink)}
.canvas{position:relative;width:1200px;height:965px}

.slide,.doc-page{position:absolute;background:var(--page);box-shadow:0 2px 6px rgba(0,0,0,.25);overflow:hidden}
.slide{width:400px;height:285px}
.doc-page{width:337px}

/* brand wordmark */
.wordmark{font-weight:700;color:var(--brand);letter-spacing:1px;line-height:1}
.wordmark-tag{font-size:6px;color:var(--muted);letter-spacing:.3px;margin-top:2px}

/* title slide */
.title-logo{position:absolute;left:22px;top:20px}
.title-logo .wordmark{font-size:32px}
.hero-band{position:absolute;left:0;right:0;top:92px;height:118px;background:linear-gradient(180deg,var(--brand-light) 0%,var(--brand) 45%,var(--brand-dark) 100%)}
.hero-visual{position:absolute;left:0;top:0;width:150px;height:100%;background:linear-gradient(135deg,#b9d7f0 0%,#4f8fd0 55%,#1b4f93 100%)}
.hero-text{position:absolute;left:170px;top:36px;color:#fff}
.hero-title{font-size:17px;font-weight:600;letter-spacing:.4px}
.hero-sub{font-size:11px;font-style:italic;margin-top:2px}
.hero-swoosh{position:absolute;left:0;top:190px;width:400px;height:40px}
.slide-foot-logo{position:absolute;left:14px;bottom:10px;font-size:11px}
.thanks{position:absolute;left:170px;top:48px;color:#fff;font-size:13px;font-style:italic}

/* content slides */
.slide-header{position:absolute;left:0;right:0;top:0;height:50px}
.slide-title{position:absolute;left:16px;top:16px;font-size:12px;font-weight:700;color:var(--brand);text-transform:uppercase;letter-spacing:.3px}
.header-visual{position:absolute;right:0;top:0;width:92px;height:50px;border-bottom-left-radius:46px;background:linear-gradient(135deg,#d6e8f7 0%,#4f8fd0 60%,#1b4f93 100%)}
.header-rule{position:absolute;left:0;right:0;top:50px;height:3px;background:linear-gradient(90deg,var(--brand-dark),var(--brand-light))}
.slide-footer{position:absolute;left:0;right:0;bottom:0;height:20px;background:linear-gradient(90deg,var(--brand-dark),var(--brand) 60%,var(--brand-light))}
.slide-footer .wordmark{position:absolute;left:12px;top:5px;font-size:9px;color:#fff}
.bullets{position:absolute;list-style:none;font-size:9px;line-height:1.32;color:var(--ink)}
.bullets li{position:relative;padding-left:12px;margin-bottom:7px}
.bullets li::before{content:"";position:absolute;left:0;top:4px;width:6px;height:6px;background:var(--brand)}
.bullets.compact{font-size:7.6px}
.groups{position:absolute;left:218px;top:66px;width:170px;list-style:none;font-size:6.6px;line-height:1.3}
.groups li{position:relative;padding-left:10px;margin-bottom:5px}
.groups li::before{content:"";position:absolute;left:0;top:2px;width:5px;height:5px;background:var(--brand)}
.groups b{display:block;color:var(--brand);font-size:7.5px}
.chart{position:absolute}

/* word pages */
.doc-logo{position:absolute;left:0;right:0;top:34px;text-align:center}
.doc-logo .wordmark{font-size:34px}
.doc-band{position:absolute;left:0;right:0;top:150px;height:150px;background:linear-gradient(180deg,var(--brand-light),var(--brand) 50%,var(--brand-dark))}
.doc-visual{position:absolute;left:0;top:0;width:140px;height:100%;background:linear-gradient(135deg,#c4ddf2,#4f8fd0 55%,#1b4f93)}
.doc-band-title{position:absolute;left:158px;top:64px;color:#fff;font-size:13px;letter-spacing:.5px}
.doc-web{position:absolute;left:0;right:0;bottom:22px;text-align:center;font-size:6px;color:var(--muted)}
.doc-foot{position:absolute;left:0;right:0;bottom:0;height:10px;background:linear-gradient(90deg,var(--brand-dark),var(--brand-light))}
.doc-head{position:absolute;left:16px;top:14px}
.doc-head .wordmark{font-size:13px}
.doc-head-rule{position:absolute;left:0;right:0;top:38px;height:2px;background:var(--rule)}
.doc-heading{position:absolute;left:16px;top:52px;font-size:11px;color:var(--brand);letter-spacing:.4px}
.doc-text{position:absolute;left:16px;right:16px;font-size:5.6px;line-height:1.35;color:var(--ink)}
.doc-text p{margin-bottom:4px}
.doc-text.indent{left:130px}
.doc-figure{position:absolute;left:30px;top:150px;width:280px;height:140px;background:linear-gradient(135deg,#eef5fc 0%,var(--sky) 60%,#a9cbeb 100%)}
</style>
</head>
<body>
<main class="canvas">

  <section class="slide title-slide" style="left:13px;top:12px">
    <div class="title-logo"><div class="wordmark">DLPN</div><div class="wordmark-tag">Delpine Lane Partners Network</div></div>
    <div class="hero-band">
      <div class="hero-visual" role="img" aria-label="Cloud computing and technology imagery"></div>
      <div class="hero-text"><div class="hero-title">TITLE OF PRESENTATION</div><div class="hero-sub">Subtitle of Presentation</div></div>
    </div>
    <svg class="hero-swoosh" viewBox="0 0 400 40" preserveAspectRatio="none"><path d="M0 20 C120 40 260 0 400 14 L400 40 L0 40Z" fill="#fff"/><path d="M0 20 C120 40 260 0 400 14" fill="none" stroke="var(--rule)" stroke-width="2"/></svg>
    <div class="slide-foot-logo wordmark">DLPN</div>
  </section>

  <section class="slide" style="left:437px;top:12px">
    <div class="slide-header"><h2 class="slide-title">Corporate Profile</h2><div class="header-visual" role="img" aria-label="Technology imagery"></div></div>
    <div class="header-rule"></div>
    <ul class="bullets" style="left:40px;top:66px;width:330px">
      <li>DELPINE LANE PARTNERS NETWORK (DLPN) is a management consulting &amp; business intelligence company that designs and implements information technology solutions to deliver business advantage to federal, state, local and corporate clients. (DLPN) is a certified Small Disadvantaged Business (DBE) and Veteran Owned Small Business (VOSB)</li>
      <li>DLPN has the talent and expertise to function as a prime contractor or a participating subcontractor fulfilling legal requirements for minority/disadvantaged portions of major government contracts.</li>
    </ul>
    <div class="slide-footer"><span class="wordmark">DLPN</span></div>
  </section>

  <section class="slide" style="left:13px;top:370px">
    <div class="slide-header"><h2 class="slide-title">Corporate Profile</h2><div class="header-visual" role="img" aria-label="Technology imagery"></div></div>
    <div class="header-rule"></div>
    <svg class="chart" style="left:14px;top:66px" width="195" height="180" viewBox="0 0 195 180">
      <g stroke="#ddd" stroke-width="1"><line x1="20" y1="20" x2="190" y2="20"/><line x1="20" y1="55" x2="190" y2="55"/><line x1="20" y1="90" x2="190" y2="90"/><line x1="20" y1="125" x2="190" y2="125"/></g>
      <line x1="20" y1="160" x2="190" y2="160" stroke="#888"/><line x1="20" y1="10" x2="20" y2="160" stroke="#888"/>
      <g fill="var(--brand)"><rect x="34" y="98" width="22" height="62"/><rect x="76" y="64" width="22" height="96"/><rect x="118" y="44" width="22" height="116"/><rect x="160" y="78" width="22" height="82"/></g>
      <g font-size="6" fill="#555" text-anchor="middle"><text x="45" y="170">Group1</text><text x="87" y="170">Group2</text><text x="129" y="170">Group3</text><text x="171" y="170">Group4</text></g>
      <g font-size="6" fill="#555" text-anchor="end"><text x="16" y="162">0</text><text x="16" y="127">5</text><text x="16" y="92">10</text><text x="16" y="57">15</text><text x="16" y="22">20</text></g>
    </svg>
    <ul class="groups">
      <li><b>Group1</b>Lorem ipsum dolor sit amet, consectetur adipiscing elit, sed do eiusmod tempor incididunt ut labore.</li>
      <li><b>Group2</b>Ut enim ad minim veniam, quis nostrud exercitation ullamco laboris nisi ut aliquip ex ea.</li>
      <li><b>Group3</b>Duis aute irure dolor in reprehenderit in voluptate velit esse cillum dolore fugiat nulla.</li>
      <li><b>Group4</b>Excepteur sint occaecat cupidatat non proident, sunt in culpa qui officia deserunt mollit anim.</li>
    </ul>
    <div class="slide-footer"><span class="wordmark">DLPN</span></div>
  </section>

  <section class="slide" style="left:437px;top:370px">
    <div class="slide-header"><h2 class="slide-title">Corporate Profile</h2><div class="header-visual" role="img" aria-label="Technology imagery"></div></div>
    <div class="header-rule"></div>
    <svg class="chart" style="left:14px;top:64px" width="190" height="190" viewBox="0 0 190 190">
      <ellipse cx="95" cy="62" rx="78" ry="30" fill="#0c3a7a"/>
      <path d="M95 56 L95 26 A78 30 0 0 1 172 60 Z" fill="var(--brand-light)"/>
      <path d="M95 56 L172 60 A78 30 0 0 1 60 84 Z" fill="var(--brand)"/>
      <path d="M95 56 L60 84 A78 30 0 0 1 25 42 Z" fill="#9fc2e6"/>
      <g stroke="#ddd"><line x1="15" y1="120" x2="180" y2="120"/><line x1="15" y1="145" x2="180" y2="145"/></g>
      <line x1="15" y1="170" x2="180" y2="170" stroke="#888"/>
      <g fill="var(--brand)"><rect x="30" y="130" width="20" height="40"/><rect x="72" y="112" width="20" height="58"/><rect x="114" y="138" width="20" height="32"/><rect x="156" y="120" width="20" height="50"/></g>
    </svg>
    <ul class="bullets compact" style="left:218px;top:64px;width:170px">
      <li>DELPINE LANE PARTNERS NETWORK (DLPN) is a management consulting &amp; business intelligence company that designs and implements information technology solutions to deliver business advantage to federal, state, local and corporate clients.</li>
      <li>DLPN has the talent and expertise to function as a prime contractor or a participating subcontractor fulfilling legal requirements for minority/disadvantaged portions of major government contracts.</li>
    </ul>
    <div class="slide-footer"><span class="wordmark">DLPN</span></div>
  </section>

  <section class="slide title-slide" style="left:225px;top:670px">
    <div class="title-logo"><div class="wordmark">DLPN</div><div class="wordmark-tag">Delpine Lane Partners Network</div></div>
    <div class="hero-band">
      <div class="hero-visual" role="img" aria-label="Cloud computing and technology imagery"></div>
      <div class="thanks">Thank you for your attention</div>
    </div>
    <svg class="hero-swoosh" viewBox="0 0 400 40" preserveAspectRatio="none"><path d="M0 20 C120 40 260 0 400 14 L400 40 L0 40Z" fill="#fff"/><path d="M0 20 C120 40 260 0 400 14" fill="none" stroke="var(--rule)" stroke-width="2"/></svg>
  </section>

  <section class="doc-page" style="left:853px;top:12px;height:450px">
    <div class="doc-logo"><div class="wordmark">DLPN</div><div class="wordmark-tag">Delpine Lane Partners Network</div></div>
    <div class="doc-band">
      <div class="doc-visual" role="img" aria-label="Cloud and technology imagery"></div>
      <div class="doc-band-title">CORPORATE MANUALS</div>
    </div>
    <div class="doc-web">www.dlpn-us.com</div>
    <div class="doc-foot"></div>
  </section>

  <section class="doc-page" style="left:853px;top:495px;height:455px">
    <div class="doc-head"><span class="wordmark">DLPN</span></div>
    <div class="doc-head-rule"></div>
    <h2 class="doc-heading">CORPORATE MANUALS</h2>
    <div class="doc-text indent" style="top:76px">
      <p>DELPINE LANE PARTNERS NETWORK (DLPN) is a management consulting &amp; business intelligence company that designs and implements information technology solutions to deliver business advantage to federal, state, local and corporate clients.</p>
      <p>DLPN has the talent and expertise to function as a prime contractor or a participating subcontractor fulfilling legal requirements.</p>
    </div>
    <div class="doc-figure" role="img" aria-label="Network infrastructure illustration"></div>
    <div class="doc-text" style="top:305px">
      <p>DELPINE LANE PARTNERS NETWORK (DLPN) is a management consulting &amp; business intelligence company that designs and implements information technology solutions to deliver business advantage to federal, state, local and corporate clients. (DLPN) is a certified Small Disadvantaged Business and Veteran Owned Small Business.</p>
      <p>DLPN has the talent and expertise to function as a prime contractor or a participating subcontractor fulfilling legal requirements for minority/disadvantaged portions of major government contracts.</p>
    </div>
    <div class="doc-foot"></div>
  </section>

</main>
</body>
</html>
```